Trading Cards

I want someone to design custom trading cards for my pro wrestling gig.

Target Market(s)

Pro wrestling fans

Requirements
Must have
• I will upload 8 photos. I need a card for each.
Nice to have
• I would like the card trimmed out on silver and feature the Storm Vault Logo I uploaded on the top center. The back of the card can be black with the same logo centered.

```html
<!DOCTYPE html>
<html lang="en">
<head>
<meta charset="utf-8">
<title>Storm Vault Wrestling – Trading Card Front and Back</title>
<link href="https://fonts.googleapis.com/css2?family=Montserrat:wght@600&family=Oswald:wght@500;700&display=swap" rel="stylesheet">
<style>
  :root {
    --stage-light: #a9a9a9;
    --stage-dark: #6f6f6f;
    --heading-white: #ffffff;
    --card-black: #050505;
    --brand-red: #d9161e;
    --brand-red-dark: #8c0a10;
    --brand-yellow: #f7d417;
    --silver-light: #f2f2f2;
    --silver-mid: #b9b9b9;
    --silver-dark: #8a8a8a;
  }
  html, body {
    margin: 0;
    padding: 0;
    width: 1200px;
    height: 1200px;
    overflow: hidden;
  }
  .canvas {
    position: relative;
    width: 1200px;
    height: 1200px;
    background: radial-gradient(ellipse at 40% 30%, var(--stage-light) 0%, #8d8d8d 55%, var(--stage-dark) 100%);
    overflow: hidden;
  }
  .presentation-note {
    position: absolute;
    top: 140px;
    left: 0;
    width: 1160px;
    margin: 0;
    text-align: center;
    font-family: "Montserrat", sans-serif;
    font-weight: 600;
    font-size: 25px;
    letter-spacing: 0.16em;
    color: var(--heading-white);
  }
  .card {
    position: absolute;
    top: 232px;
    width: 526px;
    height: 736px;
  }
  .card--front { left: 58px; }
  .card--back { left: 616px; }
  .card-art {
    position: absolute;
    inset: 0;
    width: 100%;
    height: 100%;
  }
  .brand-mark {
    position: absolute;
    left: 0;
    width: 100%;
    text-align: center;
    font-family: "Oswald", sans-serif;
    font-weight: 700;
    color: var(--brand-yellow);
    text-transform: uppercase;
    line-height: 0.95;
  }
  .brand-mark span { display: block; }
  .card--front .brand-mark { top: 74px; }
  .card--front .brand-mark .brand-name { font-size: 48px; letter-spacing: 0.02em; }
  .card--front .brand-mark .brand-sub { font-size: 50px; letter-spacing: 0.04em; }
  .card--back .brand-mark { top: 288px; }
  .card--back .brand-mark .brand-name { font-size: 66px; letter-spacing: 0.02em; }
  .card--back .brand-mark .brand-sub { font-size: 70px; letter-spacing: 0.05em; }
  .wrestler-name {
    position: absolute;
    top: 559px;
    left: 0;
    width: 100%;
    margin: 0;
    text-align: center;
    font-family: "Oswald", sans-serif;
    font-weight: 500;
    font-size: 62px;
    line-height: 1;
    color: var(--brand-red);
    text-transform: uppercase;
    letter-spacing: 0.01em;
  }
  .weight-class {
    position: absolute;
    left: 0;
    width: 100%;
    text-align: center;
    font-family: "Oswald", sans-serif;
    font-weight: 500;
    color: var(--brand-yellow);
    text-transform: uppercase;
    line-height: 1;
  }
  .card--front .weight-class { top: 646px; font-size: 18px; letter-spacing: 0.65em; padding-left: 0.65em; }
  .card--back .weight-class { top: 584px; font-size: 24px; letter-spacing: 0.7em; padding-left: 0.7em; }
</style>
</head>
<body>
<main class="canvas">
  <p class="presentation-note">Will make all the card same</p>

  <article class="card card--front">
    <svg class="card-art" viewBox="0 0 847 1185" preserveAspectRatio="none" aria-hidden="true">
      <defs>
        <linearGradient id="silver-face" x1="0" y1="0" x2="1" y2="1">
          <stop offset="0" stop-color="#e9e9e9"/>
          <stop offset="0.35" stop-color="#c9c9c9"/>
          <stop offset="0.55" stop-color="#f4f4f4"/>
          <stop offset="0.8" stop-color="#bdbdbd"/>
          <stop offset="1" stop-color="#dedede"/>
        </linearGradient>
        <linearGradient id="silver-trim" x1="0" y1="0" x2="1" y2="0">
          <stop offset="0" stop-color="#8a8a8a"/>
          <stop offset="0.3" stop-color="#f2f2f2"/>
          <stop offset="0.6" stop-color="#a5a5a5"/>
          <stop offset="1" stop-color="#eeeeee"/>
        </linearGradient>
        <linearGradient id="photo-tone" x1="0" y1="0" x2="0" y2="1">
          <stop offset="0" stop-color="#050505"/>
          <stop offset="0.3" stop-color="#1a1a12"/>
          <stop offset="0.6" stop-color="#5a2a22"/>
          <stop offset="1" stop-color="#1c1414"/>
        </linearGradient>
      </defs>
      <rect class="card-base" x="0" y="0" width="847" height="1185" rx="34" fill="url(#silver-face)"/>
      <path class="frame-outer" fill="#050505"
        d="M54,102 L195,102 L230,67 L620,67 L655,102 L793,102 L793,320 L770,345 L770,860 L793,885 L793,1067 L655,1067 L620,1115 L230,1115 L195,1067 L54,1067 L54,890 L75,865 L75,345 L54,320 Z"/>
      <rect class="photo-slot" x="92" y="130" width="664" height="908" fill="url(#photo-tone)" role="img" aria-label="Photo of the wrestler posing with championship belts"/>
      <path class="frame-trim" fill="none" stroke="url(#silver-trim)" stroke-width="5"
        d="M78,124 L205,124 L240,89 L610,89 L645,124 L771,124 L771,310 L748,335 L748,870 L771,895 L771,1052 L650,1052 L618,1092 L232,1092 L200,1052 L76,1052 L76,900 L97,875 L97,335 L78,310 Z"/>
      <path class="name-plate" fill="#050505" stroke="url(#silver-trim)" stroke-width="9"
        d="M145,888 L705,888 L724,908 L736,955 L724,1002 L705,1022 L145,1022 L126,1002 L114,955 L126,908 Z"/>
      <path class="name-plate-inner" fill="none" stroke="#9a9a9a" stroke-width="3"
        d="M155,902 L695,902 L710,918 L720,955 L710,992 L695,1008 L155,1008 L140,992 L130,955 L140,918 Z"/>
    </svg>
    <div class="brand-mark"><span class="brand-name">Storm Vault</span><span class="brand-sub">Wrestling</span></div>
    <h2 class="wrestler-name">Iron Havoc</h2>
    <div class="weight-class">Heavyweight</div>
  </article>

  <article class="card card--back">
    <svg class="card-art" viewBox="0 0 847 1185" preserveAspectRatio="none" aria-hidden="true">
      <defs>
        <radialGradient id="back-glow" cx="0.5" cy="0.5" r="0.7">
          <stop offset="0" stop-color="#050505"/>
          <stop offset="0.7" stop-color="#141414"/>
          <stop offset="1" stop-color="#3a3a3a"/>
        </radialGradient>
        <linearGradient id="red-trim" x1="0" y1="0" x2="1" y2="1">
          <stop offset="0" stop-color="#e0161f"/>
          <stop offset="0.5" stop-color="#8c0a10"/>
          <stop offset="1" stop-color="#e0161f"/>
        </linearGradient>
      </defs>
      <rect class="card-base" x="0" y="0" width="847" height="1185" rx="34" fill="url(#back-glow)"/>
      <path class="frame-panel" fill="#050505"
        d="M48,102 L190,102 L215,72 L640,72 L665,102 L800,102 L800,700 L780,730 L780,840 L800,870 L800,1090 L665,1090 L640,1120 L215,1120 L190,1090 L48,1090 L48,860 L70,830 L70,360 L48,330 Z"/>
      <path class="frame-red" fill="none" stroke="url(#red-trim)" stroke-width="16"
        d="M48,102 L190,102 L215,72 L640,72 L665,102 L800,102 L800,700 L780,730 L780,840 L800,870 L800,1090 L665,1090 L640,1120 L215,1120 L190,1090 L48,1090 L48,860 L70,830 L70,360 L48,330 Z"/>
      <path class="frame-silver" fill="none" stroke="#bdbdbd" stroke-width="4"
        d="M72,126 L200,126 L225,96 L630,96 L655,126 L776,126 L776,692 L756,722 L756,848 L776,878 L776,1066 L655,1066 L630,1096 L225,1096 L200,1066 L72,1066 L72,868 L94,838 L94,352 L72,322 Z"/>
    </svg>
    <div class="brand-mark"><span class="brand-name">Storm Vault</span><span class="brand-sub">Wrestling</span></div>
    <div class="weight-class">Heavyweight</div>
  </article>
</main>
</body>
</html>
```